KPV Construction we build lodges in Botswana

We need a Design Layout only with Categories where we can update each projects photos.... We have a web address and a host - kpv.construction

```html
<!DOCTYPE html>
<html lang="en">
<head>
<meta charset="utf-8">
<title>KPV Construction</title>
<link rel="stylesheet" href="https://fonts.googleapis.com/css2?family=Audiowide&family=Great+Vibes&family=Lora&family=Roboto:wght@400;700&display=swap">
<style>
:root{
  --blue:#1565c4;
  --blue-deep:#0c3f86;
  --red:#f2344c;
  --red-deep:#c8102e;
  --white:#ffffff;
  --ink:#0b1430;
  --nav-ink:#1b2540;
  --panel:rgba(40,22,12,.72);
}
*{box-sizing:border-box;margin:0;padding:0}
html,body{width:1200px;height:3072px;overflow:hidden}
body{font-family:"Roboto",Arial,sans-serif;background:var(--ink)}
.page{position:relative;width:1200px;height:3072px;overflow:hidden}
.abs{position:absolute}

/* hero */
.hero{left:0;top:0;width:1200px;height:651px;
  background:linear-gradient(180deg,#9fb7d6 0%,#c8c6c2 12%,#7c8e7a 30%,#5a7a3c 50%,#6d8a44 68%,#8a6a88 86%,#6a5a6a 100%)}
.hero-glow{left:0;top:0;width:1200px;height:651px;
  background:radial-gradient(ellipse 260px 140px at 600px 90px,rgba(255,240,200,.85),rgba(255,240,200,0) 70%),
             radial-gradient(ellipse 900px 200px at 600px 560px,rgba(170,90,150,.45),rgba(170,90,150,0) 70%)}
.navbar{left:0;top:0;width:1200px;height:102px;background:rgba(235,240,248,.55)}
.brand{left:82px;top:34px;display:flex;align-items:center;gap:10px;
  font-family:"Audiowide",sans-serif;font-size:22px;color:var(--blue)}
.brand-mark{width:18px;height:18px;background:var(--red)}
.nav{left:604px;top:28px;display:flex;align-items:center;font-size:11px;font-weight:700;color:var(--nav-ink)}
.nav a{display:block;text-decoration:none;color:inherit;padding:0 14px;line-height:46px}
.nav .active{background:var(--blue);color:var(--white);border:2px solid #6fb2ff;line-height:42px;font-size:9px}
.cart{left:1068px;top:30px;display:flex;align-items:center;gap:10px;font-size:11px;font-weight:700;color:var(--nav-ink)}
.cart-icon{width:40px;height:40px;border-radius:50%;border:2px solid var(--nav-ink);display:flex;align-items:center;justify-content:center}
.hero-title{left:0;top:285px;width:1200px;text-align:center;font-family:"Audiowide",sans-serif;font-size:78px;font-weight:400;
  letter-spacing:2px;color:#c6d0e0;text-shadow:0 2px 0 #5d6c88,0 4px 8px rgba(0,0,0,.5)}
.cta{left:483px;top:450px;width:258px;height:54px;border-radius:8px;border:2px solid #8fc4ff;
  background:linear-gradient(180deg,#3f8cf0,#1452c2);color:var(--white);font-family:"Audiowide",sans-serif;
  font-size:24px;display:flex;align-items:center;justify-content:center;box-shadow:0 0 14px rgba(40,120,255,.7)}

/* showcase */
.showcase{left:0;top:651px;width:1200px;height:1342px;
  background:linear-gradient(200deg,var(--red) 0%,#b2466e 22%,#6a58a4 40%,var(--blue) 62%,var(--blue) 100%)}
.slide-side-l{left:86px;top:758px;width:260px;height:196px;background:linear-gradient(135deg,#b9743f,#6b3616)}
.slide-side-r{left:846px;top:758px;width:258px;height:196px;background:linear-gradient(135deg,#dfe6e2,#8fa39e)}
.slide-main{left:385px;top:698px;width:430px;height:314px;background:#2a2a2e;border:2px solid #555}
.slide-main-photo{left:433px;top:740px;width:334px;height:236px;background:linear-gradient(160deg,#f1ede6,#c9bfae 60%,#6c6258)}
.slide-close{left:747px;top:740px;width:18px;height:18px;border:1px solid #999;background:#ddd}
.arrow{top:836px;width:28px;height:40px}
.caption{left:0;top:1024px;width:1200px;text-align:center;font-family:"Audiowide",sans-serif;font-size:20px;letter-spacing:4px;color:var(--white)}
.caption-date{left:0;top:1046px;width:1200px;text-align:center;font-family:"Great Vibes",cursive;font-size:30px;line-height:36px;color:var(--white)}
.section-title{left:0;width:1200px;text-align:center;font-family:"Audiowide",sans-serif;font-size:36px;font-weight:400;color:var(--white);letter-spacing:2px}
.section-title .blue{color:var(--blue);text-shadow:0 0 2px #fff}
.section-title .red{color:var(--red)}
.gallery{left:72px;top:1167px;width:1046px;height:680px;display:grid;grid-template-columns:repeat(3,1fr);grid-template-rows:repeat(3,1fr);
  gap:4px;background:#3a3a44;border:2px solid #555}
.tile{border:1px solid rgba(255,255,255,.2)}
.dots{left:528px;top:1862px;display:flex;gap:8px}
.dot{width:11px;height:11px;border-radius:50%;background:#aab4c6}
.dot.on{background:var(--blue)}

/* articles */
.articles{left:0;top:1993px;width:1200px;height:287px;background:#555}
.article{top:1993px;height:287px;padding:30px 32px;color:var(--white)}
.article p{font-family:"Lora",serif;font-size:19px;line-height:28px}
.article small{display:block;margin-top:14px;font-size:11px}

/* newsletter */
.newsletter{left:0;top:2284px;width:1200px;height:655px;
  background:linear-gradient(180deg,#b8c4cf 0%,#7d8fa4 12%,#b69a64 22%,#d3a157 38%,#c3873f 50%,#5d7ea8 58%,#c98d45 68%,#a66b2e 85%,#7b4e24 100%)}
.news-title{left:389px;top:2406px;font-family:"Audiowide",sans-serif;font-size:16px}
.news-title .b{color:var(--blue)}.news-title .r{color:var(--red)}
.news-input{left:410px;top:2481px;font-size:15px;font-style:italic;color:var(--white)}
.news-line{left:400px;top:2510px;width:360px;height:1px;background:rgba(255,255,255,.6)}
.news-send{left:762px;top:2466px;width:67px;height:53px;background:var(--white);display:flex;align-items:center;justify-content:center}
.contact{top:2595px;width:240px;height:184px;background:var(--panel);border:2px solid rgba(0,0,0,.5);display:flex;align-items:center;justify-content:center}
.contact-tile{width:106px;height:110px;background:linear-gradient(180deg,#f4f4f4,#c9ccd0);border-radius:10px;display:flex;flex-direction:column;
  align-items:center;justify-content:center;gap:6px;font-size:12px;color:#555;box-shadow:0 4px 8px rgba(0,0,0,.5)}
.contact-tile.round{border-radius:50%;width:116px;height:116px}

/* footer */
.footer{left:0;top:2939px;width:1200px;height:133px;background:linear-gradient(180deg,#1a1f3a,#0a0f28)}
.footer-band{left:0;top:2948px;width:1200px;height:62px;background:linear-gradient(180deg,#7a0a16,var(--red-deep) 50%,#4a0510)}
.footer-glow{left:0;top:3010px;width:1200px;height:10px;background:linear-gradient(90deg,rgba(80,140,255,0),#e8f0ff 50%,rgba(80,140,255,0))}
.footer-brand{left:22px;top:2960px;display:flex;align-items:center;gap:10px;font-family:"Audiowide",sans-serif;font-size:28px;color:var(--blue)}
.footer-brand .brand-mark{width:22px;height:22px}
.social{left:380px;top:2958px;display:flex;gap:20px}
.social span{width:42px;height:42px;border-radius:50%;background:rgba(0,0,0,.25);border:1px solid rgba(255,255,255,.15)}
</style>
</head>
<body>
<div class="page">

  <section class="abs hero" role="img" aria-label="Mountain valley at sunrise with wildflowers in the foreground"></section>
  <div class="abs hero-glow"></div>
  <header class="abs navbar"></header>
  <div class="abs brand"><span class="brand-mark"></span>KPV Construction</div>
  <nav class="abs nav">
    <a class="active">HOME</a><a>GALLERY</a><a>TOP</a><a style="padding-left:40px">BLOG</a><a>CONTACT</a>
  </nav>
  <div class="abs cart">CART
    <span class="cart-icon"><svg width="22" height="20" viewBox="0 0 22 20"><path d="M1 2h4l3 11h10l3-8H6" fill="none" stroke="#1b2540" stroke-width="2"/><circle cx="9" cy="17" r="1.8" fill="#1b2540"/><circle cx="17" cy="17" r="1.8" fill="#1b2540"/></svg></span>
  </div>
  <h1 class="abs hero-title">KPV CONSTRUCTION</h1>
  <div class="abs cta">GET STARTED</div>

  <section class="abs showcase"></section>
  <div class="abs slide-side-l" role="img" aria-label="Project slide with city typography artwork"></div>
  <div class="abs slide-side-r" role="img" aria-label="Project slide with vintage city sign"></div>
  <div class="abs slide-main"></div>
  <div class="abs slide-main-photo" role="img" aria-label="Bright open-plan living room and dining area"></div>
  <div class="abs slide-close"></div>
  <svg class="abs arrow" style="left:4px" viewBox="0 0 28 40"><path d="M22 6L8 20l14 14" fill="none" stroke="#ffffff" stroke-width="5" opacity=".7"/></svg>
  <svg class="abs arrow" style="left:1168px" viewBox="0 0 28 40"><path d="M6 6l14 14L6 34" fill="none" stroke="#ffffff" stroke-width="5" opacity=".7"/></svg>
  <div class="abs caption">CITIES &amp; TYPOGRAPHY</div>
  <div class="abs caption-date">Jun 26th</div>

  <h2 class="abs section-title" style="top:1100px"><span class="blue">OUR</span> <span class="red">GALLERY</span></h2>
  <div class="abs gallery">
    <div class="tile" role="img" aria-label="Living room with dining table" style="background:linear-gradient(160deg,#cfc3b0,#6e6254)"></div>
    <div class="tile" role="img" aria-label="Dining room with art wall" style="background:linear-gradient(160deg,#bfb3a2,#5c5246)"></div>
    <div class="tile" role="img" aria-label="Bedroom with wooden platform" style="background:linear-gradient(160deg,#8a8580,#3a3633)"></div>
    <div class="tile" role="img" aria-label="Minimal white living space" style="background:linear-gradient(160deg,#e0dcd6,#8e857c)"></div>
    <div class="tile" role="img" aria-label="Lounge with dark wood wall" style="background:linear-gradient(160deg,#7a6650,#2e2824)"></div>
    <div class="tile" role="img" aria-label="Reading corner with armchair" style="background:linear-gradient(160deg,#b29c84,#4a3c30)"></div>
    <div class="tile" role="img" aria-label="Kids room with striped daybed" style="background:linear-gradient(160deg,#e8e2d8,#c07a3a)"></div>
    <div class="tile" role="img" aria-label="Sitting room with grey armchair" style="background:linear-gradient(160deg,#d6d2cc,#6e6660)"></div>
    <div class="tile" role="img" aria-label="Hallway leading to bedroom" style="background:linear-gradient(160deg,#bdb9b4,#3c3a38)"></div>
  </div>
  <div class="abs dots"><span class="dot on"></span><span class="dot"></span><span class="dot"></span><span class="dot"></span><span class="dot"></span><span class="dot"></span><span class="dot"></span><span class="dot"></span></div>

  <h2 class="abs section-title" style="top:1914px">OUR LATEST <span class="red">ARTICLES</span></h2>
  <div class="abs articles"></div>
  <article class="abs article" style="left:0;width:389px;background:linear-gradient(160deg,#5e4a3e,#2a1e18)" role="img" aria-label="Hands holding a coffee cup over a laptop">
    <p>Etiam commodo convallis quis minim veniam, quis nostrud exercitation veniam.</p><small>May 27, 2015</small>
  </article>
  <article class="abs article" style="left:397px;width:398px;background:linear-gradient(180deg,#a9b4c2,#7b8797)" role="img" aria-label="Woman in sunglasses looking into the distance">
    <p>Lorem ipsum dolor sit amet conse ctetur adipisicing elit, labore et dolore aliqua.</p><small>May 17, 2015</small>
  </article>
  <article class="abs article" style="left:801px;width:399px;background:linear-gradient(160deg,#8a847c,#4c4640)" role="img" aria-label="Person wearing a knitted yellow scarf">
    <p>Etiam commodo convallis quis minim veniam, quis nostrud exercitation veniam.</p><small>May 27, 2015</small>
  </article>

  <section class="abs newsletter" role="img" aria-label="Golden grassland with a winding stream under a cloudy sky"></section>
  <div class="abs news-title"><span class="b">SUBSCRIBE</span> <span class="r">NEWSLETTER</span></div>
  <div class="abs news-input">Enter Email To Get Notification</div>
  <div class="abs news-line"></div>
  <div class="abs news-send"><svg width="34" height="28" viewBox="0 0 34 28"><path d="M2 13L32 2 26 26 16 18 12 25 11 16z" fill="#1e88d8"/><path d="M11 16L32 2" stroke="#fff" stroke-width="1.5"/></svg></div>

  <div class="abs contact" style="left:213px"><div class="contact-tile">
    <svg width="44" height="52" viewBox="0 0 44 52"><path d="M22 4c-8 0-13 6-13 13 0 9 13 22 13 22s13-13 13-22c0-7-5-13-13-13z" fill="none" stroke="#666" stroke-width="3"/><circle cx="22" cy="17" r="5" fill="none" stroke="#666" stroke-width="3"/><path d="M4 48l8-10h20l8 10z" fill="none" stroke="#666" stroke-width="2.5"/></svg>FIND US</div></div>
  <div class="abs contact" style="left:477px"><div class="contact-tile round">
    <svg width="50" height="36" viewBox="0 0 50 36"><rect x="3" y="3" width="44" height="30" rx="3" fill="none" stroke="#666" stroke-width="3"/><path d="M3 5l22 16 22-16" fill="none" stroke="#666" stroke-width="3"/></svg>MAIL US</div></div>
  <div class="abs contact" style="left:743px"><div class="contact-tile">
    <svg width="48" height="48" viewBox="0 0 48 48"><circle cx="24" cy="22" r="19" fill="none" stroke="#666" stroke-width="3"/><path d="M16 14c0 10 8 18 18 18l3-4-5-3-3 2c-3-2-5-4-7-7l2-3-3-5z" fill="#666"/></svg>CALL US</div></div>

  <footer class="abs footer"></footer>
  <div class="abs footer-band"></div>
  <div class="abs footer-glow"></div>
  <div class="abs footer-brand"><span class="brand-mark"></span>KPV Construction</div>
  <div class="abs social"><span></span><span></span><span></span><span></span><span></span><span></span><span></span><span></span></div>

</div>
</body>
</html>
```